Plovenworks business card

We need a modern business card - With our 4 colors - See web: www.plovenworks.dk

I have attached logo and som old business Cards we have - Lets Make the new ones shine...:-) -

Industry/Entity Type

Business

Requirements
Must have
• the logo with plovnworks only,

```html
<!DOCTYPE html>
<html lang="en">
<head>
<meta charset="utf-8">
<title>Plovenworks business card</title>
<link rel="stylesheet" href="https://fonts.googleapis.com/css2?family=Open+Sans:wght@300;400;700&display=swap">
<style>
  :root {
    --backdrop: #463c37;
    --card: #1c1c1c;
    --card-back: #141414;
    --lime: #8cc63f;
    --text: #f2f2f2;
    --muted: #c9c9c9;
    --divider: #555555;
    --emboss: #9a9a9a;
  }
  * { margin: 0; padding: 0; box-sizing: border-box; }
  html, body { width: 1200px; height: 807px; overflow: hidden; }
  body {
    background: var(--backdrop);
    font-family: "Open Sans", Arial, sans-serif;
    position: relative;
  }
  .card {
    position: absolute;
    top: 249px;
    width: 540px;
    height: 309px;
    border-radius: 4px;
  }
  .card-back { left: 40px; background: var(--card-back); }
  .card-front { left: 620px; background: var(--card); }

  .wordmark {
    position: absolute;
    display: flex;
    align-items: center;
    gap: 12px;
    font-weight: 300;
    letter-spacing: 3px;
  }
  .card-back .wordmark {
    left: 50%; top: 50%;
    transform: translate(-50%, -50%);
    font-size: 34px;
    color: var(--emboss);
  }
  .card-back .wordmark .mark { width: 26px; height: 26px; border-radius: 50%; background: var(--emboss); }

  .card-front .wordmark {
    left: 34px; top: 136px;
    font-size: 25px;
    color: var(--text);
  }
  .card-front .wordmark .mark { width: 20px; height: 20px; border-radius: 50%; background: var(--lime); }

  .divider {
    position: absolute;
    left: 262px; top: 90px;
    width: 1px; height: 130px;
    background: linear-gradient(to bottom, transparent, var(--divider), transparent);
  }

  .details {
    position: absolute;
    left: 290px; top: 34px;
    right: 24px;
  }
  .name { color: var(--lime); font-weight: 700; font-size: 26px; line-height: 1.1; }
  .role { color: var(--muted); font-size: 15px; margin-bottom: 12px; }
  .address { color: var(--text); font-size: 15px; line-height: 1.35; margin-bottom: 12px; }
  .contacts { list-style: none; color: var(--text); font-size: 15px; line-height: 1.55; }
  .contacts li { display: flex; align-items: center; gap: 8px; }
  .contacts svg { width: 13px; height: 13px; flex: none; fill: var(--lime); }
</style>
</head>
<body>
  <section class="card card-back" aria-label="Card back">
    <div class="wordmark"><span class="mark"></span>plovnworks</div>
  </section>

  <section class="card card-front" aria-label="Card front">
    <div class="wordmark"><span class="mark"></span>plovnworks</div>
    <div class="divider"></div>
    <div class="details">
      <p class="name">Mads Holberg</p>
      <p class="role">Managing Member</p>
      <p class="address">418 Harbor Lane,<br>Fairhaven, CA 95720</p>
      <ul class="contacts">
        <li><svg viewBox="0 0 16 16"><path d="M3 1l3 0 1 4-2 1c1 2 3 4 5 5l1-2 4 1 0 3c0 1-1 2-2 2C7 15 1 9 1 3c0-1 1-2 2-2z"/></svg>(555) 214-3080</li>
        <li><svg viewBox="0 0 16 16"><path d="M4 1h6l2 2v3H4zM2 7h12v6H2zM5 9v2h6V9z"/></svg>(555) 214-3081</li>
        <li><svg viewBox="0 0 16 16"><path d="M4 1h8v14H4zM5.5 2.5v9h5v-9zM7 12.5h2v1H7z" fill-rule="evenodd"/></svg>(555) 708-4192</li>
        <li><svg viewBox="0 0 16 16"><path d="M1 3h14v10H1zM2 4l6 5 6-5z" fill-rule="evenodd"/></svg>mads@plovenworks.dk</li>
        <li><svg viewBox="0 0 16 16"><path d="M8 1a7 7 0 1 0 0 14A7 7 0 0 0 8 1zm0 1.5c1 1.2 1.6 3 1.7 4.7H6.3C6.4 5.5 7 3.7 8 2.5zM2.6 8.8h2.2c.1 1.6.6 3 1.3 4.1a5.5 5.5 0 0 1-3.5-4.1zm0-1.6a5.5 5.5 0 0 1 3.5-4.1c-.7 1.1-1.2 2.5-1.3 4.1zm3.7 1.6h3.4c-.1 1.7-.7 3.5-1.7 4.7-1-1.2-1.6-3-1.7-4.7zm5-1.6c-.1-1.6-.6-3-1.3-4.1a5.5 5.5 0 0 1 3.5 4.1zm0 1.6h2.1a5.5 5.5 0 0 1-3.4 4.1c.7-1.1 1.2-2.5 1.3-4.1z"/></svg>www.plovenworks.dk</li>
      </ul>
    </div>
  </section>
</body>
</html>
```